Mirvane Trinkets
Lucinda Harrow Designs
Mirvane Trinkets -
Creative Brief
Simple
Lucinda Harrow
Jewelry Designer
2719 Quillfern Ln Dallas TX 75294
lucinda@mirvane-example.com
www.mirvane-example.com
Please do a few designs!
Maybe just the logo?

```html
<!DOCTYPE html>
<html lang="en">
<head>
<meta charset="utf-8">
<title>Mirvane Trinkets – Stationery Set</title>
<link rel="stylesheet" href="https://fonts.googleapis.com/css2?family=Raleway:wght@400;600&family=Open+Sans:wght@400;600&display=swap">
<style>
  :root {
    --bg: #e9e6e2;
    --paper: #ffffff;
    --teal: #1c9f9b;
    --teal-dark: #127d7a;
    --ink: #5a5f63;
    --ink-soft: #9aa0a4;
    --silver-a: #f4f4f4;
    --silver-b: #b9bbbd;
    --shadow: 0 2px 6px rgba(0,0,0,.18);
  }
  * { box-sizing: border-box; margin: 0; padding: 0; }
  html, body { width: 1200px; height: 481px; overflow: hidden; }
  body { background: var(--bg); font-family: "Open Sans", sans-serif; color: var(--ink); position: relative; }

  .card, .letterhead, .envelope { position: absolute; box-shadow: var(--shadow); }
  .card { width: 160px; height: 104px; border-radius: 8px; background: var(--paper); overflow: hidden; }
  .card--teal { background: var(--teal); }
  .card--silver { background: radial-gradient(circle at 50% 45%, var(--silver-a), var(--silver-b)); }

  .brand { display: flex; flex-direction: column; align-items: center; gap: 2px; }
  .brand__dot { width: 14px; height: 14px; border-radius: 50%; background: var(--ink-soft); }
  .brand__name { font-family: "Raleway", sans-serif; font-weight: 600; font-size: 18px; color: var(--ink); line-height: 1; }
  .brand__sub { font-family: "Raleway", sans-serif; font-size: 5px; letter-spacing: .12em; text-transform: uppercase; color: var(--ink-soft); }
  .brand--light .brand__dot { background: #e6f5f4; }
  .brand--light .brand__name, .brand--light .brand__sub { color: #ffffff; }
  .brand--small .brand__name { font-size: 11px; }
  .brand--small .brand__dot { width: 9px; height: 9px; }

  .card__center { position: absolute; inset: 0; display: flex; align-items: center; justify-content: center; }
  .card__front .brand { position: absolute; left: 8px; top: 10px; }
  .card__stripe { position: absolute; left: 0; right: 0; bottom: 0; height: 5px; background: var(--teal); }
  .card__person { position: absolute; right: 10px; top: 12px; text-align: right; }
  .card__name { font-size: 6px; font-weight: 600; color: var(--ink); }
  .card__role { font-size: 4.5px; color: var(--teal); }
  .contact { position: absolute; right: 10px; top: 40px; text-align: right; font-size: 4.5px; line-height: 1.6; color: var(--ink); }

  .letterhead { left: 456px; top: 31px; width: 216px; height: 425px; background: var(--paper); }
  .letterhead .brand { position: absolute; left: 14px; top: 12px; align-items: flex-start; }
  .letterhead .contact { top: 14px; right: 14px; }
  .letterhead__mark { position: absolute; left: 60px; top: 150px; width: 90px; height: 90px; border-radius: 50%; background: #f3f4f4; }

  .envelope { background: var(--paper); overflow: hidden; }
  .envelope__flap { position: absolute; left: 0; top: 0; width: 100%; }
  .envelope--back { left: 696px; top: 149px; width: 487px; height: 134px; }
  .envelope--closed { left: 696px; top: 31px; width: 487px; height: 190px; }
  .envelope--front { left: 684px; top: 288px; width: 372px; height: 172px; }
  .envelope__seal { position: absolute; width: 16px; height: 16px; border-radius: 50%; background: #ffffff; }
  .envelope .contact { left: 14px; right: auto; top: 92px; text-align: left; }
  .envelope__mark { position: absolute; right: 18px; bottom: 10px; width: 60px; height: 60px; border-radius: 50%; background: #f3f4f4; }
</style>
</head>
<body>

  <!-- business card fronts -->
  <article class="card card__front" style="left:19px;top:65px">
    <div class="brand brand--small"><span class="brand__dot"></span><span class="brand__name">mirvane</span></div>
    <div class="card__person"><p class="card__name">Lucinda Harrow</p><p class="card__role">Jewelry Designer</p></div>
    <div class="contact">2719 Quillfern Ln<br>Dallas TX 75294<br>Phone (214) 555-0147<br>lucinda@mirvane-example.com<br>www.mirvane-example.com</div>
    <div class="card__stripe"></div>
  </article>
  <article class="card card__front" style="left:192px;top:65px">
    <div class="brand brand--small"><span class="brand__dot"></span><span class="brand__name">mirvane</span></div>
    <div class="card__person"><p class="card__name">Lucinda Harrow</p><p class="card__role">Jewelry Designer</p></div>
    <div class="contact">2719 Quillfern Ln<br>Dallas TX 75294<br>Phone (214) 555-0147<br>lucinda@mirvane-example.com<br>www.mirvane-example.com</div>
    <div class="card__stripe"></div>
  </article>

  <!-- card backs -->
  <article class="card card--silver" style="left:19px;top:192px">
    <div class="card__center"><span class="brand__dot" style="width:34px;height:34px;background:#d6d7d8"></span></div>
  </article>
  <article class="card card--teal" style="left:192px;top:192px">
    <div class="card__center"><span class="brand__dot" style="width:34px;height:34px;background:#e6f5f4"></span></div>
  </article>
  <article class="card card--teal" style="left:19px;top:305px">
    <div class="card__center"><div class="brand brand--light"><span class="brand__dot"></span><span class="brand__name">mirvane</span><span class="brand__sub">Lucinda Harrow Designs</span></div></div>
  </article>
  <article class="card" style="left:192px;top:305px">
    <div class="card__center"><div class="brand"><span class="brand__dot"></span><span class="brand__name">mirvane</span><span class="brand__sub">Lucinda Harrow Designs</span></div></div>
  </article>

  <!-- letterhead -->
  <section class="letterhead">
    <div class="brand brand--small"><span class="brand__dot"></span><span class="brand__name">mirvane</span><span class="brand__sub">Lucinda Harrow Designs</span></div>
    <div class="contact">2719 Quillfern Ln<br>Dallas TX 75294<br>Phone (214) 555-0147<br>lucinda@mirvane-example.com<br>www.mirvane-example.com</div>
    <div class="letterhead__mark"></div>
  </section>

  <!-- envelopes -->
  <section class="envelope envelope--back">
    <svg class="envelope__flap" width="487" height="134" viewBox="0 0 487 134">
      <path d="M0 0 L243 70 L487 0" fill="none" stroke="#dcdcdc" stroke-width="1"/>
    </svg>
  </section>
  <section class="envelope envelope--closed">
    <svg class="envelope__flap" width="487" height="190" viewBox="0 0 487 190">
      <path d="M0 0 H487 V20 Q360 30 300 80 Q250 100 190 80 Q120 30 0 20 Z" fill="var(--teal)"/>
    </svg>
    <span class="envelope__seal" style="left:236px;top:66px"></span>
  </section>
  <section class="envelope envelope--front">
    <svg class="envelope__flap" width="372" height="172" viewBox="0 0 372 172">
      <path d="M0 0 H372 V40 Q330 36 300 30 Q220 18 160 22 Q100 30 0 58 Z" fill="var(--teal)"/>
    </svg>
    <span class="envelope__seal" style="left:20px;top:30px"></span>
    <div class="contact">2719 Quillfern Ln<br>Dallas TX 75294<br>Phone (214) 555-0147<br>lucinda@mirvane-example.com<br>www.mirvane-example.com</div>
    <div class="envelope__mark"></div>
  </section>

</body>
</html>
```